Owen Tasker Studios Business Card

Looking for a clear, modern, elegant, sharp business card that conveys a professional yet edgy image to my business as a wedding, portrait, and travel photographer. Would like something that looks vintage yet modern. Need a new business card to grow my business. We are growing the business for Wedding and Event Photography as well as fine art Photography. (Mostly Landscapes)
Updates

I’m looking through designs now but I have a new logo that i want using please.

New logo uploaded please redesign using that

PLEASE ALL DESIGNERS LOOK IN BRIEF FOR NEW LOGO

Target Market(s)

Brides, Grooms, Families with Kids, People looking for Fine Art Photography Artwork

Industry/Entity Type

Photographer

Contact Information for Business Card

Unsure

Font styles to use
Serif

Colors

Designer to choose colors to be used in the design.

Requirements
Must have
• My Website:
• http://taskerlens.examplefolio.net
• Phone:
• 323-481-5206
• Email:
• owentaskerlens@mailbox-example.net
Nice to have
• Would like a sort of shine on the printing finish.
• I like black I think it looks good on a business card.
• Can try working with my logo (png that I've attached)

```html
<!DOCTYPE html>
<html lang="en">
<head>
<meta charset="utf-8">
<title>Owen Tasker Studios Business Card</title>
<link rel="stylesheet" href="https://fonts.googleapis.com/css2?family=Montserrat:wght@300;400&display=swap">
<style>
  :root {
    --page-bg: #ecebe8;
    --card-light: #ffffff;
    --card-dark: #050608;
    --ink-dark: #141414;
    --ink-light: #d9dadc;
    --card-shadow: rgba(0, 0, 0, 0.14);
  }
  * { box-sizing: border-box; margin: 0; padding: 0; }
  html, body {
    width: 1200px;
    height: 800px;
    overflow: hidden;
    background: var(--page-bg);
    font-family: "Montserrat", "Helvetica Neue", Arial, sans-serif;
  }
  .canvas {
    width: 1200px;
    height: 800px;
    display: flex;
    align-items: center;
    justify-content: center;
    gap: 48px;
  }
  .card {
    width: 525px;
    height: 300px;
    border-radius: 3px;
    box-shadow: 0 10px 28px var(--card-shadow);
    display: flex;
    flex-direction: column;
    align-items: center;
    justify-content: center;
  }
  .card--front { background: var(--card-light); color: var(--ink-dark); }
  .card--back { background: var(--card-dark); color: var(--ink-light); }

  .brand { text-align: center; }
  .brand__name {
    font-weight: 400;
    font-size: 30px;
    letter-spacing: 0.16em;
    text-transform: uppercase;
    margin-right: -0.16em;
  }
  .brand__tagline {
    margin-top: 8px;
    font-weight: 400;
    font-size: 10px;
    letter-spacing: 0.5em;
    text-transform: uppercase;
    margin-right: -0.5em;
  }

  .contact {
    list-style: none;
    text-align: center;
    font-weight: 400;
    font-size: 14px;
    line-height: 1.75;
    letter-spacing: 0.03em;
  }
</style>
</head>
<body>
  <main class="canvas">
    <section class="card card--front" aria-label="Business card front">
      <div class="brand">
        <p class="brand__name">Owen Tasker</p>
        <p class="brand__tagline">Studios</p>
      </div>
    </section>

    <section class="card card--back" aria-label="Business card back">
      <ul class="contact">
        <li class="contact__web">taskerlens.examplefolio.net</li>
        <li class="contact__phone">323-481-5206</li>
        <li class="contact__email">owentaskerlens@mailbox-example.net</li>
      </ul>
    </section>
  </main>
</body>
</html>
```